Craft Instant Coffee Box Packaging design

We need packaging designed for our craft instant coffee. Needs to be simple yet eye-catching. We are looking to package instant coffee sachets inside a cigarette style box. Front of box must make it clear that it is instant coffee and show contents - 7 pack / 21g net as well as Drift Willow Roasters Co. which is the company name. We'd prefer the instant coffee be the focal point rather than the company name. The rear will have 'ingredients', company address and barcode. Sides should either state contents such as 'Instant Coffee' or company name.

Font styles to use
Sans Serif

Colors

Designer to choose colors to be used in the design.

Requirements
Must have
• Front of box must make it clear that it is instant coffee and show contents - 7 pack / 21g net as well as Drift Willow Roasters Co. which is the company name. We'd prefer the instant coffee be the focal point rather than the company name. The rear will have 'ingredients', company address and barcode. Sides should either state contents such as 'Instant Coffee' or company name.
Nice to have
• modern colour scheme - 'Drift Willow Roasters Co.' in a simple sans serif font
Should not have
• Must not be too 'busy' or 'cheap' looking

```html
<!DOCTYPE html>
<html lang="id">
<head>
<meta charset="utf-8">
<title>Drift Willow Roasters Co. – Instant Coffee Box</title>
<link href="https://fonts.googleapis.com/css2?family=Montserrat:wght@300;400;600;700&display=swap" rel="stylesheet">
<style>
  :root {
    --bg: #ececec;
    --box-dark: #1c1410;
    --box-brown-light: #b48a62;
    --box-brown-mid: #6b4630;
    --box-brown-deep: #2a1a12;
    --band-red: #cc3a42;
    --band-red-dark: #9e242b;
    --gold: #e3c36e;
    --white: #ffffff;
    --soft-white: #e7e2dc;
  }
  * { margin: 0; padding: 0; box-sizing: border-box; }
  html, body { width: 978px; height: 1200px; overflow: hidden; background: var(--bg); }
  body { font-family: "Montserrat", Arial, sans-serif; position: relative; }

  .dieline { position: absolute; left: 40px; top: 60px; width: 898px; height: 1080px; display: flex; }

  /* Side panel */
  .side-panel {
    width: 220px; height: 100%; position: relative;
    background: linear-gradient(180deg, #3a2a20 0%, var(--box-dark) 45%, #0e0a08 100%);
  }
  .side-panel .band {
    position: absolute; left: 0; top: 240px; width: 100%; height: 160px;
    background: var(--band-red-dark);
  }
  .serving {
    position: absolute; left: 30px; top: 500px; width: 170px; color: var(--soft-white);
  }
  .serving-title {
    display: inline-block; border: 1px solid var(--soft-white);
    font-size: 11px; letter-spacing: 1px; padding: 3px 8px; margin-bottom: 26px; font-weight: 400;
  }
  .step { margin-bottom: 34px; }
  .step svg { display: block; margin-bottom: 10px; }
  .step p { font-size: 12px; font-weight: 300; line-height: 1.3; }

  /* Front panel */
  .front-panel {
    flex: 1; height: 100%; position: relative; overflow: hidden;
    background: linear-gradient(180deg, var(--box-brown-light) 0%, var(--box-brown-mid) 35%, var(--box-brown-deep) 70%, #120c09 100%);
  }
  .brand {
    position: absolute; top: 180px; width: 100%; text-align: center;
    color: var(--white); font-size: 26px; font-weight: 400; white-space: nowrap;
  }
  .brand strong { font-weight: 700; }
  .front-panel .band {
    position: absolute; left: 0; top: 240px; width: 100%; height: 160px;
    background: var(--band-red);
    display: flex; align-items: center; justify-content: center;
  }
  .product-name {
    color: var(--gold); font-size: 86px; font-weight: 600; letter-spacing: -1px;
    line-height: 1; white-space: nowrap;
  }
  .hero-art {
    position: absolute; left: 140px; top: 420px; width: 540px; height: 600px;
    background: radial-gradient(ellipse at 50% 55%, #d9c7b5 0%, #a0693a 30%, #4a2c1b 60%, rgba(30,18,12,0) 80%);
  }
  .contents-tag {
    position: absolute; left: 30px; bottom: 0; width: 130px; height: 60px;
    background: var(--band-red); color: var(--white);
    font-size: 15px; font-weight: 400; display: flex; align-items: center; justify-content: center;
  }
</style>
</head>
<body>
  <main class="dieline">
    <section class="side-panel">
      <div class="band"></div>
      <div class="serving">
        <span class="serving-title">CARA PENYAJIAN</span>
        <div class="step">
          <svg width="48" height="48" viewBox="0 0 48 48" fill="none" stroke="#e7e2dc" stroke-width="2">
            <path d="M8 4h14v16"/><path d="M10 26h26v8a10 10 0 0 1-10 10h-6a10 10 0 0 1-10-10z"/><path d="M36 29h4a4 4 0 0 1 0 8h-5"/><path d="M6 46h34"/>
          </svg>
          <p>Tuang satu sachet<br>ke dalam cangkir.</p>
        </div>
        <div class="step">
          <svg width="48" height="48" viewBox="0 0 48 48" fill="none" stroke="#e7e2dc" stroke-width="2">
            <path d="M4 10l12-6 8 14-12 6z"/><path d="M14 26h24v8a9 9 0 0 1-9 9h-6a9 9 0 0 1-9-9z"/><path d="M38 29h3a3.5 3.5 0 0 1 0 7h-4"/><path d="M24 14q2 4 0 8"/>
          </svg>
          <p>Tuang air mendidih.</p>
        </div>
        <div class="step">
          <svg width="48" height="48" viewBox="0 0 48 48" fill="none" stroke="#e7e2dc" stroke-width="2">
            <path d="M32 4l-10 22"/><path d="M10 26h26v8a10 10 0 0 1-10 10h-6a10 10 0 0 1-10-10z"/><path d="M36 29h4a4 4 0 0 1 0 8h-5"/><path d="M18 14q-2 4 0 8"/>
          </svg>
          <p>Aduk merata.<br>Nikmati selagi panas.</p>
        </div>
      </div>
    </section>

    <section class="front-panel">
      <p class="brand"><strong>DRIFT WILLOW</strong> Roasters Co.</p>
      <div class="band">
        <h1 class="product-name">Instant Coffee</h1>
      </div>
      <div class="hero-art" role="img" aria-label="Coffee pouring into a steaming glass cup surrounded by roasted coffee beans"></div>
      <div class="contents-tag">7 pack / 21g</div>
    </section>
  </main>
</body>
</html>
```